Business Cards

We are an innovating group of real estate investors who buy beat up house's, fix them up, and resell them. We are in need of a business card that is catchy and stands out. We want it to say something like " We buy house's cash fast" Call us first

Industry/Entity Type

Business

Requirements
Must have
• Our logo which is updated

```html
<!DOCTYPE html>
<html lang="en">
<head>
<meta charset="utf-8">
<title>BrightTurn Business Cards</title>
<link rel="stylesheet" href="https://fonts.googleapis.com/css2?family=Lato:wght@400;700&family=Ubuntu:wght@400;700&display=swap">
<style>
  :root {
    --stage: #23281f;
    --card: #3b3b3d;
    --card-band: #353537;
    --lime: #8dc63f;
    --lime-dark: #7cb32f;
    --plum: #9a3fa6;
    --text-light: #e6e6e6;
    --white: #ffffff;
    --stripe-grey: #bdbdbd;
  }
  * { margin: 0; padding: 0; box-sizing: border-box; }
  html, body { width: 1200px; height: 900px; overflow: hidden; }
  body {
    position: relative;
    background: var(--stage);
    font-family: "Lato", Arial, sans-serif;
  }
  .card {
    position: absolute;
    width: 668px;
    height: 388px;
    background: var(--card);
    box-shadow: 6px 8px 18px rgba(0,0,0,.55);
    overflow: hidden;
  }
  .card--front { left: 77px; top: 40px; }
  .card--back { left: 470px; top: 463px; }

  .card__stripe {
    position: absolute; left: 0; right: 0;
    top: 325px; height: 15px;
    background: linear-gradient(var(--stripe-grey) 0 3px, var(--white) 3px 7px, var(--stripe-grey) 7px 10px, var(--white) 10px 15px);
  }
  .card__band {
    position: absolute; left: 0; right: 0;
    top: 340px; bottom: 0;
    background: linear-gradient(var(--lime), var(--lime-dark));
  }

  .brand {
    position: absolute;
    display: flex; align-items: center; gap: 14px;
  }
  .brand__mark {
    width: 26px; height: 26px;
    background: var(--lime);
  }
  .brand__name {
    font-family: "Lato", Arial, sans-serif;
    font-weight: 700;
    color: var(--plum);
    font-size: 40px;
    letter-spacing: .5px;
  }
  .card--front .brand { left: 96px; top: 138px; }

  .contact {
    position: absolute; left: 0; right: 0;
    top: 233px; height: 90px;
    background: var(--card-band);
  }
  .contact__item {
    position: absolute;
    display: flex; align-items: center; gap: 8px;
    font-size: 13.5px; color: var(--text-light);
    letter-spacing: .2px;
  }
  .contact__item svg { width: 14px; height: 14px; fill: var(--lime); flex: none; }
  .contact__item--name { left: 44px; top: 24px; }
  .contact__item--address { left: 44px; top: 58px; }
  .contact__item--phone { left: 256px; top: 24px; }
  .contact__item--fax { left: 256px; top: 59px; }
  .contact__item--web { left: 458px; top: 25px; }
  .contact__item--email { left: 458px; top: 59px; }

  .card--back .brand {
    left: 0; right: 0; top: 118px;
    justify-content: center;
  }
  .card--back .brand__name { font-size: 34px; }
  .tagline {
    position: absolute; left: 0; right: 0;
    text-align: center;
    font-family: "Ubuntu", Arial, sans-serif;
    color: var(--white);
  }
  .tagline--main {
    top: 180px;
    font-size: 33px; font-weight: 700;
    letter-spacing: -.5px;
  }
  .tagline--call {
    top: 228px;
    font-size: 28px; font-weight: 400;
    letter-spacing: 3px;
  }
</style>
</head>
<body>

  <section class="card card--front" aria-label="Business card front">
    <div class="brand">
      <span class="brand__mark"></span>
      <span class="brand__name">BrightTurn</span>
    </div>

    <div class="contact">
      <div class="contact__item contact__item--name">
        <svg viewBox="0 0 14 14"><circle cx="7" cy="4" r="3.2"/><path d="M1.5 14c0-4 2.5-6 5.5-6s5.5 2 5.5 6z"/></svg>
        <span>Name and Surname</span>
      </div>
      <div class="contact__item contact__item--address">
        <svg viewBox="0 0 14 14"><path d="M7 0a4.8 4.8 0 0 0-4.8 4.8C2.2 8.3 7 14 7 14s4.8-5.7 4.8-9.2A4.8 4.8 0 0 0 7 0zm0 7a2.2 2.2 0 1 1 0-4.4A2.2 2.2 0 0 1 7 7z"/></svg>
        <span>Address</span>
      </div>
      <div class="contact__item contact__item--phone">
        <svg viewBox="0 0 14 14"><path d="M4 1h3l-1 3-1.5 1c.6 1.8 1.7 3 3.5 3.7l1-1.5 3 .8v3c0 1-.8 1.5-1.8 1.3C5.5 11.5 2.2 8 1.8 3 1.7 2 2.5 1 3.5 1z"/></svg>
        <span>Telephone</span>
      </div>
      <div class="contact__item contact__item--fax">
        <svg viewBox="0 0 14 14"><path d="M3.5 1h7v3.5h-7zM1 5.5h12V11h-2.5v2h-7v-2H1zM4.5 9v3h5V9z"/></svg>
        <span>Fax</span>
      </div>
      <div class="contact__item contact__item--web">
        <svg viewBox="0 0 14 14"><circle cx="7" cy="7" r="6.5"/><path d="M4 4.5c1.5-.5 2.5.5 2 2s-2 1-2.5 2.5M9 2.5c-.5 1.5 1 2 2 2.5M8.5 11c.5-1.5 2-1.5 2.5-2.5" stroke="#353537" stroke-width="1.3" fill="none"/></svg>
        <span>www.yourwebsite.com</span>
      </div>
      <div class="contact__item contact__item--email">
        <svg viewBox="0 0 14 14"><path d="M1 3h12v8H1z" fill="none" stroke="#8dc63f" stroke-width="1.2"/><path d="M1 3l6 5 6-5" fill="none" stroke="#8dc63f" stroke-width="1.2"/></svg>
        <span>your@email.com</span>
      </div>
    </div>

    <div class="card__stripe"></div>
    <div class="card__band"></div>
  </section>

  <section class="card card--back" aria-label="Business card back">
    <div class="brand">
      <span class="brand__mark"></span>
      <span class="brand__name">BrightTurn</span>
    </div>
    <h1 class="tagline tagline--main">WE BUY HOUSE'S CASH FAST</h1>
    <p class="tagline tagline--call">CALL US FIRST</p>
    <div class="card__stripe"></div>
    <div class="card__band"></div>
  </section>

</body>
</html>
```